Vantor Grid Advisory Partners - Website

Design & Build a website for a new company which operates in the Systems and Technology space for Transportation, Government and Commercial sectors.

Overall design should be minimalist in nature.
Should also have a feed that provides news and event updates on the main page.
Logo has already been awarded and should be incorporated into the site.

We like the overall layout, functionality and simplicity of the below sites. Submitted designs could be similar to or a combination of the aspects on these sites, or perhaps a whole different concept - we are open to new ideas.
Morqeli.com
Tumb.it

All I am moving away from the Tumb.it website and would like it to be more aligned with Morqeli.com not only in layout but in functionality. I will be extending the deadline of this design brief for two weeks to incorporate additional requirements and will add addtional funding to the project.

Apologies for not having more information available to provide but with so many submissions its getting confusing.

Thanks Dorian

Important: We will need two language versions of the website, English and Arabic; the website is hosted on HostPivo

Hello All, Thank you for your submissions. We have narrowed it down to the final 6 designers and I just wanted to take a moment and provide a bit of feedback regarding the concepts that we like and the modifications we are looking for. First, let me mention some of the design functions we like. - At the top of the homepage we really like the "region" or "language" tab so that the website can be viewed in both English and Arabic. - We like the homepage to have clear color variation so that the different sections of the homepage are distinct. Additionally, we like the bottom portion of the homepage to be in red. We feel that draws attention to our contact information. Again, we would like the colors to integrate black, gray-scale, red, etc. - Having a search tab at the top of the home page, or integrated into the main image, so that the site is easy to navigate. - We especially like the main image to have the scrolling tabs at the bottom so it is easy to browse the services offered (Consultancy, Solutions Architecture, Masters Systems Integration, Independent Design Review). - In regards to the services offered tab we really like the idea that a few people presented that have the outside of our logo with an icon in the middle of consultancy, solutions, etc., etc. Secondly, as mentioned in our brief we really enjoy the design of morqeli site. Specially, we enjoy the strong iconic images they use, the way the tabs at the top scroll easily, and contact us page that generates an email. Lastly, I've included some photos of the concept we have been working on. What we are trying to demonstrate is how our company offers a range of services that are essentially linked together. We provide individual services that when combined present the full service package. We would like this concept to be integrated into the over concept of our website. Please feel free to ask for clarification of any of the above points or contact us if you have any additional questions. We appreciate all of your hard work and are very excited to see the updated designs. Best, Miriam Okaford Vangridex Senior Program Manager miriam.okaford@vangridax.example

Industry/Entity Type

Government

Font styles to use
Serif
Sans Serif

Requirements
Must have
• Must work on/adapt to various/mobile devices (responsive)
Must be simple and straightforward
Colors should be in line/matching with logo
2 language versions: English and Arabic (no Thai)
Services should be the first group/row of items after/below the main image
Note: the website will be hosted by hostpivo
Nice to have
• Submit feedback form
What's New section
The banner at the bottom of the site should not be too large; we would like a narrow one more
It would be nice if the header/top banner (with Home, About, etc. tabs) could stay in place as you scroll down (like Morqeli and Chatterly)
We will likely only use one image with a Company slogan on the Home page rather than a carousel of images to rotate through
Should not have
• This is the existing website: http://www.vangridex.example
We do not like the animation, the way the banner icons/titles bounce
Not simple enough, we don't like the functionality or how pages load so slowly
We do not like the logo centered - it should be at the left
The banner and its tabs should not be towards the right, we would like them to be centered, to go all the way across and to be below the logo

```html
<!DOCTYPE html>
<html lang="en">
<head>
<meta charset="utf-8">
<title>Vangridex International</title>
<link href="https://fonts.googleapis.com/css2?family=Lato:wght@300;400;700;900&display=swap" rel="stylesheet">
<style>
:root{
  --red:#e31e24;
  --ink:#2e3338;
  --text:#555b60;
  --muted:#9aa1a6;
  --line:#e3e6e8;
  --panel:#f0f3f5;
  --footer:#2d3439;
  --footer-deep:#262b30;
  --footer-text:#8f979d;
  --white:#ffffff;
}
*{margin:0;padding:0;box-sizing:border-box}
html,body{width:1016px;height:1200px;overflow:hidden}
body{position:relative;font-family:'Lato',sans-serif;color:var(--text);background:var(--white)}
.abs{position:absolute}
a{color:inherit;text-decoration:none}

/* top bar */
.topbar{left:0;top:0;width:1016px;height:19px;border-bottom:1px solid var(--line);font-size:7.5px;color:var(--muted)}
.topbar-items{position:absolute;right:198px;top:4px;display:flex;gap:16px}
.topbar .item{display:flex;align-items:center;gap:6px;white-space:nowrap}
.topbar svg{stroke:var(--ink);fill:none;stroke-width:1;flex:none}

/* header */
.header{left:0;top:19px;width:1016px;height:59px;border-bottom:1px solid var(--line)}
.brand{position:absolute;left:219px;top:19px;display:flex;align-items:center;gap:8px}
.brand-square{width:14px;height:14px;background:var(--red)}
.brand-name{font-size:13px;font-weight:700;letter-spacing:2px;color:var(--red);line-height:1}
.nav a{position:absolute;top:24px;font-size:9px;color:var(--ink)}

/* hero */
.hero{left:0;top:78px;width:1016px;height:317px;background:linear-gradient(90deg,#f4f4f3 0%,#e6dfd9 20%,#c9b7a8 40%,#8a8480 55%,#6f7a86 75%,#5d86b8 90%,#9fb6cf 100%)}
.hero-panel{left:517px;top:78px;width:301px;height:317px;background:rgba(105,110,112,.88)}
.hero-kicker{left:552px;top:150px;font-size:19px;font-weight:300;color:var(--red);letter-spacing:.3px}
.hero-title{left:552px;top:170px;font-size:32px;font-weight:900;color:var(--white);letter-spacing:.5px}
.hero-copy{left:552px;top:221px;width:240px;font-size:11.3px;line-height:18px;font-weight:300;color:var(--white)}
.hero-btn{left:552px;top:293px;width:95px;height:25px;border:1px solid var(--white);color:var(--white);font-size:8.5px;display:flex;align-items:center;justify-content:center}
.hero-arrow{top:218px;width:38px;height:37px;background:rgba(80,80,80,.6);display:flex;align-items:center;justify-content:center}
.hero-arrow svg{stroke:var(--white);stroke-width:1.6;fill:none}

/* services */
.section-title{font-size:19px;font-weight:300;color:var(--ink)}
.service{top:466px;width:180px;text-align:center}
.service-icon{width:78px;height:78px;margin:0 auto;display:block}
.service h3{margin-top:17px;font-size:10px;font-weight:700;color:var(--ink)}
.service p{margin-top:9px;font-size:8px;line-height:12.5px;color:var(--muted)}
.service .more{display:block;margin-top:7px;font-size:7px;color:var(--text)}

/* panel */
.panel{left:0;top:680px;width:1016px;height:335px;background:var(--panel);border-top:1px solid var(--line)}
.welcome-photo{left:198px;top:760px;width:300px;height:107px;background:linear-gradient(180deg,#3d5f96 0%,#2a3d68 55%,#1b2238 100%)}
.welcome-copy{left:198px;top:890px;width:300px;font-size:8px;line-height:12.7px;color:var(--muted)}
.welcome-copy p+p{margin-top:13px}
.news{left:519px;width:300px;height:90px}
.news-thumb{position:absolute;left:0;top:0;width:87px;height:90px;border-top:2px solid var(--ink)}
.news-date{position:absolute;left:8px;top:0;width:29px;height:34px;background:var(--ink);color:var(--white);text-align:center}
.news-date small{display:block;font-size:6px;padding-top:3px}
.news-date b{display:block;font-size:16px;font-weight:300;line-height:16px}
.news h4{position:absolute;left:106px;top:0;width:194px;font-size:11.3px;font-weight:400;line-height:16.5px;color:var(--ink)}
.news p{position:absolute;left:106px;top:40px;width:180px;font-size:7.5px;line-height:12.7px;color:var(--muted)}

/* footer */
.footer{left:0;top:1015px;width:1016px;height:147px;background:var(--footer)}
.footer-brand{left:216px;top:1070px;width:120px;text-align:center;color:var(--white)}
.footer-brand .name{font-size:16px;font-weight:900;letter-spacing:4px}
.footer-brand .sub{font-size:7.5px;letter-spacing:2.5px;margin-top:3px}
.footer h5{position:absolute;font-size:9.5px;font-weight:700;color:var(--white)}
.footer-list{font-size:8px;color:var(--footer-text)}
.footer-list li{list-style:none;height:19px;display:flex;align-items:center;gap:6px}
.footer-note{left:499px;top:1069px;width:150px;font-size:7.6px;line-height:13.5px;color:var(--footer-text)}
.sub-input{left:499px;top:1110px;width:103px;height:23px;background:var(--footer-deep);color:#c5cbd0;font-size:8px;padding-left:7px;display:flex;align-items:center}
.sub-btn{left:602px;top:1110px;width:56px;height:23px;background:var(--red);color:var(--white);font-size:8px;display:flex;align-items:center;justify-content:center}
.contact svg{fill:none;stroke:var(--footer-text);stroke-width:1.2;flex:none}
.bottombar{left:0;top:1162px;width:1016px;height:38px;background:var(--footer-deep);font-size:7px;color:var(--footer-text)}
</style>
</head>
<body>

<div class="abs topbar">
  <div class="topbar-items">
    <div class="item">
      <svg width="13" height="9" viewBox="0 0 13 9"><rect x="3" y=".5" width="9.5" height="8"/><path d="M3 .5l4.75 4 4.75-4M0 3h2M0 5h2"/></svg>
      <span>hello@vangridex.example</span>
    </div>
    <div class="item">
      <svg width="10" height="10" viewBox="0 0 10 10"><path d="M2 1l2 2-1 1.5c.7 1.3 1.6 2.2 2.5 2.5L7 6l2 2-1.2 1.3C5 9 1 5 .8 2.2z"/></svg>
      <span>+00 555 010 482</span>
    </div>
  </div>
</div>

<header class="abs header">
  <a class="brand" href="#">
    <span class="brand-square"></span>
    <span class="brand-name">VANGRIDEX</span>
  </a>
  <nav class="nav">
    <a href="#" style="left:443px">Home</a>
    <a href="#" style="left:496px">Business Units</a>
    <a href="#" style="left:582px">Services</a>
    <a href="#" style="left:643px">About Us</a>
    <a href="#" style="left:709px">Locations</a>
    <a href="#" style="left:775px">Contact Us</a>
  </nav>
</header>

<section>
  <div class="abs hero" role="img" aria-label="Photo of two smiling colleagues in a bright office"></div>
  <div class="abs hero-panel"></div>
  <div class="abs hero-kicker">SYSTEM KNOWLEDGE</div>
  <div class="abs hero-title">DELIVERED</div>
  <p class="abs hero-copy">Vangridex specializes in delivering quality professional services and technical projects that support larger business goals.</p>
  <a class="abs hero-btn" href="#">LEARN MORE</a>
  <a class="abs hero-arrow" href="#" style="left:0"><svg width="10" height="14" viewBox="0 0 10 14"><path d="M7 2L2 7l5 5"/></svg></a>
  <a class="abs hero-arrow" href="#" style="left:978px"><svg width="10" height="14" viewBox="0 0 10 14"><path d="M3 2l5 5-5 5"/></svg></a>
</section>

<section>
  <h2 class="abs section-title" style="left:0;width:1016px;text-align:center;top:420px">Our Services</h2>

  <div class="abs service" style="left:232px">
    <svg class="service-icon" viewBox="0 0 78 78"><circle cx="39" cy="39" r="30" fill="none" stroke="var(--ink)" stroke-width="6"/><rect x="28" y="36" width="18" height="8" rx="2" fill="var(--ink)"/><path d="M31 36l2-5h8l2 5z" fill="var(--ink)"/><circle cx="32" cy="45" r="2" fill="var(--ink)"/><circle cx="42" cy="45" r="2" fill="var(--ink)"/><rect x="40" y="31" width="12" height="7" rx="1.5" fill="var(--ink)"/></svg>
    <h3>Transportation</h3>
    <p>Fusce gravida tortor felis<br>Ac dictum risus sagittis id morbi posu<br>justo eleifend libero ultricies</p>
    <a class="more" href="#">LEAR MORE</a>
  </div>

  <div class="abs service" style="left:419px">
    <svg class="service-icon" viewBox="0 0 78 78"><circle cx="39" cy="39" r="30" fill="none" stroke="var(--ink)" stroke-width="6"/><path d="M30 35l9-5 9 5z" fill="var(--ink)"/><rect x="31" y="36" width="2.5" height="8" fill="var(--ink)"/><rect x="35.5" y="36" width="2.5" height="8" fill="var(--ink)"/><rect x="40" y="36" width="2.5" height="8" fill="var(--ink)"/><rect x="44.5" y="36" width="2.5" height="8" fill="var(--ink)"/><rect x="29" y="45" width="20" height="2.5" fill="var(--ink)"/></svg>
    <h3>Government</h3>
    <p>Fusce gravida tortor felis<br>Ac dictum risus sagittis id morbi posu<br>justo eleifend libero ultricies</p>
    <a class="more" href="#">LEAR MORE</a>
  </div>

  <div class="abs service" style="left:605px">
    <svg class="service-icon" viewBox="0 0 78 78"><circle cx="39" cy="39" r="30" fill="none" stroke="var(--ink)" stroke-width="6"/><rect x="32" y="29" width="14" height="19" fill="var(--ink)"/><g fill="var(--white)"><rect x="34" y="31" width="3" height="2"/><rect x="41" y="31" width="3" height="2"/><rect x="34" y="35" width="3" height="2"/><rect x="41" y="35" width="3" height="2"/><rect x="34" y="39" width="3" height="2"/><rect x="41" y="39" width="3" height="2"/><rect x="37.5" y="43" width="3" height="5"/></g></svg>
    <h3>Commercial Sectors</h3>
    <p>Fusce gravida tortor felis<br>Ac dictum risus sagittis id morbi posu<br>justo eleifend libero ultricies</p>
    <a class="more" href="#">LEAR MORE</a>
  </div>
</section>

<section>
  <div class="abs panel"></div>
  <h2 class="abs section-title" style="left:198px;top:722px">Welcome to Vangridex International</h2>
  <div class="abs welcome-photo" role="img" aria-label="Photo of a city skyline at dusk with lit towers"></div>
  <div class="abs welcome-copy">
    <p>Maecenas bibendum lacus gravida placerat consequat. Vivamus quis hendrerit mauris. Vestibulum laoreet felis sed consectetur sollicitudin. Sed a mauris massa.</p>
    <p>Nullam interdum, elit nec facilisis iaculis, arcu enim condimentum tellus, ut convallis elit purus eu est. Interdum et malesuada fames ac ante ipsum primis in faucibus. Nullam odio nulla, commodo a dui at, pretium iaculis quam.</p>
  </div>

  <h2 class="abs section-title" style="left:519px;top:722px">Latest News</h2>

  <article class="abs news" style="top:760px">
    <div class="news-thumb" role="img" aria-label="Photo of hands reviewing papers on a desk" style="background:linear-gradient(135deg,#e9e9e7,#c9c6c2)"></div>
    <div class="news-date"><small>oct</small><b>18</b></div>
    <h4>Lorem ipsum dolor sit amet, consectetur adipiscing</h4>
    <p>Maecenas bibendum lacus gravida placerat consequat. Vivamus quis hendrerit mauris. Vestibulum laoreet felis sed consectetur sollicitudin.</p>
  </article>

  <article class="abs news" style="top:867px">
    <div class="news-thumb" role="img" aria-label="Photo of two colleagues meeting in an office" style="background:linear-gradient(135deg,#dcdad6,#8a9aa8 60%,#c9d27a)"></div>
    <div class="news-date"><small>oct</small><b>18</b></div>
    <h4>Lorem ipsum dolor sit amet, consectetur adipiscing</h4>
    <p>Maecenas bibendum lacus gravida placerat consequat. Vivamus quis hendrerit mauris. Vestibulum laoreet felis sed consectetur sollicitudin.</p>
  </article>
</section>

<footer>
  <div class="abs footer">
    <h5 style="left:392px;top:32px">Navigation</h5>
    <h5 style="left:499px;top:32px">Newsletter</h5>
    <h5 style="left:691px;top:32px">Contact Details</h5>
  </div>
  <div class="abs footer-brand">
    <div class="name">VANGRIDEX</div>
    <div class="sub">INTERNATIONAL</div>
  </div>
  <ul class="abs footer-list" style="left:392px;top:1068px">
    <li>› <a href="#">Home</a></li>
    <li>› <a href="#">Services</a></li>
    <li>› <a href="#">About</a></li>
    <li>› <a href="#">Blog</a></li>
  </ul>
  <p class="abs footer-note">Ipsum dolor sit amet, teft consecte tur adipiscing elit ut eunt.</p>
  <div class="abs sub-input">Email Address</div>
  <a class="abs sub-btn" href="#">Subscribe</a>
  <ul class="abs footer-list contact" style="left:692px;top:1068px">
    <li><svg width="11" height="11" viewBox="0 0 10 10"><path d="M2 1l2 2-1 1.5c.7 1.3 1.6 2.2 2.5 2.5L7 6l2 2-1.2 1.3C5 9 1 5 .8 2.2z"/></svg>+1800-123-4567</li>
    <li><svg width="11" height="9" viewBox="0 0 11 9"><rect x=".6" y=".6" width="9.8" height="7.8"/><path d="M.6.6l4.9 4 4.9-4"/></svg>info@yourwebsite.com</li>
    <li style="align-items:flex-start;height:auto;line-height:12.5px"><svg width="11" height="12" viewBox="0 0 10 12"><path d="M5 11S1 6.5 1 4a4 4 0 018 0c0 2.5-4 7-4 7z"/><circle cx="5" cy="4" r="1.4"/></svg><span>Your Address, Your Country<br>Your Zip Code</span></li>
  </ul>
  <div class="abs bottombar">
    <span class="abs" style="left:198px;top:14px">Copyright © 2014 - Vangridex International. All Rights reserved</span>
    <span class="abs" style="left:695px;top:14px"><a href="#">Privacy Policy</a> &nbsp;|&nbsp; <a href="#">Sitemap</a></span>
  </div>
</footer>

</body>
</html>
```